Tidewell Grove Vitamin C Serum

We need a product label and box designed for our Vitamin C Serum product. The label will go on a 2oz bottle and the box will hold the 2oz bottle. Attached are the box and label templates as well as a Vitamin C Serum we have with another brand.

For this brand, we're looking to have the product look high end/luxury.

Target Market(s)

40+ year old women

```html
<!DOCTYPE html>
<html lang="en">
<head>
<meta charset="utf-8">
<title>Solvara Vitamin C Serum – Box and Label Artwork</title>
<link rel="stylesheet" href="https://fonts.googleapis.com/css2?family=Anton&family=Arimo:wght@400;700&family=Libre+Baskerville:wght@700&family=Montserrat:wght@500;700&display=swap">
<style>
  :root {
    --ink: #121212;
    --paper: #ffffff;
    --orange: #f26a10;
    --gold: #f0a818;
    --yellow: #f7c51c;
    --cut: #2fe63a;
    --fold: #e3262b;
    --muted: #d8d8d8;
  }
  * { margin: 0; padding: 0; box-sizing: border-box; }
  html, body { width: 1200px; height: 1200px; overflow: hidden; background: var(--paper); }
  .canvas { position: relative; width: 1200px; height: 1200px; overflow: hidden; background: var(--paper); }
  .artboard {
    position: absolute; left: 0; top: -269px;
    width: 1932px; height: 1932px;
    transform: scale(0.621); transform-origin: 0 0;
    font-family: "Arimo", Arial, sans-serif; color: var(--paper);
  }
  .abs { position: absolute; }
  .dieline { position: absolute; left: 0; top: 0; width: 1932px; height: 1932px; }

  .panel { position: absolute; background: var(--ink); overflow: hidden; }
  .panel--flap { border: 8px solid var(--yellow); border-left: none; border-radius: 0 26px 26px 0; }
  .burst {
    position: absolute; border-radius: 50%;
    background: radial-gradient(circle, rgba(255,255,255,0.05) 0 22%, rgba(150,150,150,0.22) 23% 26%, rgba(120,120,120,0.12) 27% 60%, rgba(0,0,0,0) 70%);
  }
  .strip { position: absolute; background: var(--paper); border-left: 8px solid var(--yellow); }

  .brand { font-family: "Libre Baskerville", Georgia, serif; font-weight: 700; color: var(--ink); }
  .vertical { writing-mode: vertical-rl; white-space: nowrap; }
  .premium { font-family: "Montserrat", Arial, sans-serif; font-weight: 500; color: var(--gold); }
  .vitc { font-family: "Anton", Impact, sans-serif; color: var(--orange); line-height: 1; }
  .serum { font-family: "Libre Baskerville", Georgia, serif; font-weight: 700; color: var(--paper); line-height: 1; }
  .size { font-weight: 700; font-size: 11px; }

  .benefits { font-size: 15px; line-height: 15px; color: var(--paper); }
  .bullets { display: flex; gap: 6px; }
  .bullets span { width: 8px; height: 8px; border-radius: 50%; background: var(--gold); display: block; }

  .maker { text-align: center; font-size: 11px; line-height: 17px; }
  .maker h3 { font-size: 12.5px; font-weight: 700; letter-spacing: 0.3px; }
  .badge { position: absolute; border: 2px solid var(--paper); }

  .usage { font-size: 8.6px; line-height: 14px; }
  .usage b { font-weight: 700; font-size: 9.5px; }

  .label-top { background: var(--paper); }
  .label-band { background: var(--yellow); }
  .label-copy { font-size: 13px; line-height: 16px; }
  .label-copy h4 { font-size: 15px; font-weight: 700; }
  .ingredients { font-size: 11.2px; line-height: 13.4px; }
  .private { font-family: "Montserrat", Arial, sans-serif; font-weight: 700; letter-spacing: 4px; font-size: 15px; }
</style>
</head>
<body>
<main class="canvas">
  <div class="artboard">

    <svg class="dieline" viewBox="0 0 1932 1932" aria-hidden="true">
      <path d="M285 983 H880 L955 1010 V1168 H1075 Q1120 1168 1120 1215 V1320 Q1120 1365 1075 1365 H955 V1380 H860 V1790 L860 1808 H305 L305 1735 L285 1548 L213 1530 V1380 H120 Q45 1380 45 1300 V1245 Q45 1165 120 1165 H213 V1010 Z" fill="none" stroke="var(--cut)" stroke-width="2"/>
      <path d="M298 997 H870 L940 1022 V1180 H1045 V1365 H1075 Q1105 1365 1105 1320 V1225 Q1105 1182 1060 1182 M845 1790 V1378 M845 1790 H318 L318 1735 L300 1548 L226 1532 V1365 H125 Q62 1365 62 1300 V1245 Q62 1182 125 1182 H226 V1022 Z" fill="none" stroke="var(--fold)" stroke-width="1.6"/>
      <line x1="308" y1="1178" x2="860" y2="1178" stroke="var(--fold)" stroke-width="1"/>
      <line x1="308" y1="1365" x2="860" y2="1365" stroke="var(--fold)" stroke-width="1"/>
      <line x1="308" y1="1546" x2="860" y2="1546" stroke="var(--fold)" stroke-width="1"/>
      <line x1="858" y1="1180" x2="858" y2="1365" stroke="var(--fold)" stroke-width="1"/>
      <line x1="1045" y1="1180" x2="1045" y2="1365" stroke="var(--fold)" stroke-width="1"/>
    </svg>

    <!-- Box: top flap with maker details -->
    <section class="panel panel--flap" style="left:308px;top:997px;width:542px;height:178px;">
      <div class="burst" role="img" aria-label="Soft radiating dot pattern" style="left:300px;top:-30px;width:200px;height:200px;"></div>
      <div class="abs vertical" style="left:20px;top:18px;font-size:12px;">www.TidewellGrove.com</div>
      <div class="abs maker" style="left:60px;top:9px;width:380px;">
        <h3>MANUFACTURED FOR AND DISTRIBUTED BY:</h3>
        <p>Tidewell Grove LLC</p>
        <p>1420 W. Harbor Ln Ste 210</p>
        <p>&nbsp;</p>
        <p>Mesa Verde, AZ 85000</p>
        <p>Lot # &amp; expiration date printed</p>
        <p>on bottom of bottle V2R1</p>
      </div>
      <div class="badge" role="img" aria-label="Not tested on animals badge" style="left:140px;top:138px;width:32px;height:32px;border-radius:50%;"></div>
      <div class="badge" role="img" aria-label="Recycle badge" style="left:240px;top:138px;width:32px;height:32px;border-radius:50%;"></div>
      <div class="badge" role="img" aria-label="Made in USA badge" style="left:344px;top:138px;width:30px;height:30px;"></div>
    </section>

    <!-- Box: front panel -->
    <section class="panel" style="left:308px;top:1180px;width:482px;height:185px;">
      <div class="burst" role="img" aria-label="Soft radiating dot pattern" style="left:80px;top:-10px;width:210px;height:210px;"></div>
      <div class="abs bullets" style="left:26px;top:18px;"><span></span><span></span><span></span><span></span><span></span><span></span><span></span></div>
      <div class="abs vertical benefits" style="left:22px;top:34px;">205 Vitamin C<br>985 Naturally Derived<br>Hyaluronic Acid<br>Vitamin E<br>Oegamic Aloe<br>Repair Fine Lines<br>Younger Looking Skin</div>
      <div class="abs premium" style="left:150px;top:20px;font-size:28px;letter-spacing:14px;">PREMIUM</div>
      <div class="abs vitc" style="left:145px;top:52px;font-size:64px;">Vitamin C</div>
      <div class="abs serum" style="left:345px;top:118px;font-size:32px;">Serum</div>
      <div class="abs size" style="left:390px;top:164px;">2 fl. Oz (60 mL)</div>
    </section>
    <div class="strip" style="left:785px;top:1172px;width:73px;height:193px;">
      <div class="abs vertical brand" style="left:12px;top:14px;font-size:30px;">Solvara</div>
      <div class="abs" style="left:22px;top:140px;width:26px;height:26px;border-radius:50%;background:var(--orange);"></div>
    </div>

    <!-- Box: top tuck -->
    <section class="abs" style="left:858px;top:1180px;width:187px;height:185px;">
      <div class="abs vertical brand" style="left:100px;top:44px;font-size:26px;">Solvara</div>
      <div class="abs" style="left:133px;top:14px;width:22px;height:22px;border-radius:50%;background:var(--orange);"></div>
      <div class="abs vertical premium" style="left:84px;top:52px;font-size:10px;letter-spacing:5px;">PREMIUM</div>
      <div class="abs vertical vitc" style="left:50px;top:20px;font-size:32px;">Vitamin C</div>
      <div class="abs vertical serum" style="left:18px;top:50px;font-size:24px;color:var(--ink);">Serum</div>
    </section>

    <!-- Box: back panel with directions -->
    <section class="panel panel--flap" style="left:308px;top:1372px;width:542px;height:170px;">
      <div class="burst" role="img" aria-label="Soft radiating dot pattern" style="left:240px;top:-20px;width:200px;height:200px;"></div>
      <div class="abs usage" style="left:20px;top:6px;width:470px;">
        <p><b>DIRECTION:</b> Apply 3-5 drops to clean face, neck and decollete areas prior moisturing and allow to absorb. Use in the morning and night before bed</p>
        <p style="margin-top:2px;"><b>CAUTION:</b> For external use only. do not use on broken or damaged skin. Avoid contact with eyes. If irritation or rash develops, discontinue use. Keep out of reach of children.</p>
        <p style="margin-top:2px;"><b>INGREDIEENT:</b></p>
        <p>Deionized Aqua (Water), Organic Aloe Bberbadensis Leaf ( Aloe), Sodium Ascorbyl Phosphate ( Vitamin C ) Methylsulfonylmethone(MSM), Cassis Angusifolia Seed Polysaccharide (Botanical hyaluronic Acid) Hamamelis Virginiana (Witch Hazel), Cabomer, (2s)-2Amino-5 guanidinopentanoic Acid, Kosher Vagatable Glycerin, organic Simmondsia Chinensis (Jojoba Oil) Phenoxyethanol,Ethylhexyglycerin. D-Alpha Tocopheryl Acetate (Vitamin E), Organic Centella Asiatica ( Gotu Kola Extract) Organic Equisetum Arvense ( Horsetail Plant Extract), Organic Pelargonium Graveolens (Geranium Extract),oeganic Taraxacum Officinale (Dandelion)</p>
      </div>
    </section>

    <!-- Box: second front panel -->
    <section class="panel" style="left:308px;top:1548px;width:482px;height:187px;">
      <div class="burst" role="img" aria-label="Soft radiating dot pattern" style="left:80px;top:-10px;width:210px;height:210px;"></div>
      <div class="abs bullets" style="left:26px;top:20px;"><span></span><span></span><span></span><span></span><span></span><span></span><span></span></div>
      <div class="abs vertical benefits" style="left:22px;top:36px;">205 Vitamin C<br>985 Naturally Derived<br>Hyaluronic Acid<br>Vitamin E<br>Oegamic Aloe<br>Repair Fine Lines<br>Younger Looking Skin</div>
      <div class="abs premium" style="left:150px;top:22px;font-size:28px;letter-spacing:14px;">PREMIUM</div>
      <div class="abs vitc" style="left:145px;top:54px;font-size:64px;">Vitamin C</div>
      <div class="abs serum" style="left:345px;top:120px;font-size:32px;">Serum</div>
      <div class="abs size" style="left:390px;top:166px;">2 fl. Oz (60 mL)</div>
    </section>
    <div class="strip" style="left:785px;top:1540px;width:73px;height:195px;">
      <div class="abs vertical brand" style="left:12px;top:18px;font-size:30px;">Solvara</div>
      <div class="abs" style="left:22px;top:145px;width:26px;height:26px;border-radius:50%;background:var(--orange);"></div>
    </div>

    <!-- Bottle label -->
    <section class="abs" style="left:1008px;top:1377px;width:859px;height:428px;">
      <div class="abs label-top" style="left:0;top:0;width:859px;height:91px;"></div>
      <div class="abs brand" style="left:0;top:30px;width:859px;text-align:center;font-size:48px;">Solvara</div>
      <div class="abs" style="left:418px;top:6px;width:24px;height:24px;border-radius:50%;background:var(--orange);"></div>
      <div class="abs label-band" style="left:0;top:91px;width:859px;height:11px;"></div>
      <div class="abs" style="left:0;top:102px;width:859px;height:326px;background:var(--ink);overflow:hidden;">
        <div class="burst" role="img" aria-label="Soft radiating dot pattern" style="left:240px;top:18px;width:240px;height:240px;"></div>
        <div class="abs label-copy" style="left:17px;top:18px;width:275px;">
          <h4>Directions:</h4>
          <p>Wash and pat skin dry. Apply small amount with fingertips to freshly cleansed and toned face, neck and decollete areas (avoid direct contact with eyes). Allow time to absorb prior to moisturizer application.</p>
          <p style="margin-top:16px;">For External use only. Discontinue use if redness or irritation occurs. Avoid direct contact with eyes. <b>Keep out of reach of children. Do not use if seal is damaged or missing. Store in a cool, dark place.</b></p>
        </div>
        <div class="abs premium" style="left:0;top:94px;width:859px;text-align:center;font-size:14px;letter-spacing:7px;">PREMIUM</div>
        <div class="abs vitc" style="left:0;top:114px;width:859px;text-align:center;font-size:38px;">Vitamin C</div>
        <div class="abs serum" style="left:0;top:162px;width:859px;text-align:center;font-size:26px;">Serum</div>
        <div class="abs private" style="left:0;top:234px;width:859px;text-align:center;">PRIVATE LABELING</div>
        <div class="abs" style="left:0;top:278px;width:859px;text-align:center;font-size:19px;">2 Fl oz. (60 ml)</div>
        <div class="abs label-copy" style="left:17px;top:262px;font-weight:700;">Lot # and expiration date printed<br>on bottom of bottle &nbsp;&nbsp;&nbsp;&nbsp;V4R0</div>
        <div class="abs ingredients" style="left:587px;top:18px;width:258px;">
          <h4 style="font-size:15px;">Ingredients:</h4>
          <p>Deionized Aqua (Water), Aloe Barbadensis Leaf (Aloe), Sodium Ascorbyl Phosphate (Vitamin C), Methylsulfonylmethane (MSM), Cassia Angustifolia Seed Polysaccharide (Botanical Hyaluronic Acid), Hamamelis Virginiana (Witch Hazel), Carbomer, (2s)-2-Amino-5- guanidinopentanoic Acid, Kosher Vegetable Glycerin, Simmondsia Chinensis (Jojoba Oil), Phenoxyethanol, EthylHexylGlycerin, d-alpha Tocopheryl Acetate (Vitamin E), Centella Asiatica (Gotu Kola Extract), Equisetum Arvense (Horsetail Plant Extract), Pelargonium Graveolens (Geranium Extract), Taraxacum Officinale (Dandelion Extract).</p>
        </div>
        <div class="abs ingredients" style="left:587px;top:242px;width:258px;font-size:12px;line-height:14px;">
          <p>Distributed By:</p>
          <p><b>Company Name</b></p>
          <p>Street Address, City, UT Zipcode</p>
          <p><b>phone number</b></p>
        </div>
      </div>
    </section>

  </div>
</main>
</body>
</html>
```